KJ Automation - Stationery and Identity.

Corporate Identity Design for the company, which includes Power Point presentations, Letterheads, business cards and mail signatures. We look for a simple design, but modern and elegant, that goes hand in hand with the technology that is the engine of the company.

Target Market(s)

Industrial Sector of Automation, Robotics and Process Control.

Industry/Entity Type

Automation

Colors

Designer to choose colors to be used in the design.

Requirements
Must have
• It must have an elegant, simple and clean design.

```html
<!DOCTYPE html>
<html lang="en">
<head>
<meta charset="UTF-8">
<title>KJ Automation – Business Cards</title>
<link href="https://fonts.googleapis.com/css2?family=Open+Sans:wght@300;400;600;700&display=swap" rel="stylesheet">
<style>
  :root {
    --bg: #e6e8eb;
    --blue: #1d9ad8;
    --blue-light: #2aa8e2;
    --blue-dark: #1a5d9c;
    --grey: #a3a5a8;
    --grey-text: #8e9094;
    --white: #ffffff;
  }
  * { margin: 0; padding: 0; box-sizing: border-box; }
  html, body { width: 1200px; height: 892px; overflow: hidden; }
  body {
    background: var(--bg);
    font-family: "Open Sans", Arial, sans-serif;
    position: relative;
  }
  .card {
    position: absolute;
    width: 560px;
    height: 320px;
    overflow: hidden;
    box-shadow: 0 10px 28px rgba(0,0,0,0.18);
  }

  /* Back of card */
  .card-back {
    left: 70px;
    top: 90px;
    background: linear-gradient(160deg, var(--blue-light), var(--blue));
  }
  .card-back .brand {
    position: absolute;
    right: 40px;
    bottom: 78px;
    display: flex;
    align-items: center;
    gap: 10px;
    color: var(--white);
    font-weight: 600;
    font-size: 24px;
    letter-spacing: 0.5px;
  }
  .brand-square {
    width: 18px;
    height: 18px;
    background: currentColor;
    flex: none;
  }
  .card-back .website {
    position: absolute;
    right: 40px;
    bottom: 40px;
    color: var(--white);
    font-size: 13px;
    font-weight: 400;
  }

  /* Front of card */
  .card-front {
    left: 570px;
    top: 482px;
    background: var(--white);
  }
  .card-front .diagonal {
    position: absolute;
    inset: 0;
  }
  .person {
    position: absolute;
    right: 72px;
    top: 24px;
    text-align: right;
    line-height: 1.05;
  }
  .person-name {
    color: var(--blue-dark);
    font-weight: 700;
    font-size: 19px;
  }
  .person-role {
    color: var(--grey-text);
    font-size: 12px;
    font-weight: 400;
    letter-spacing: 0.5px;
  }
  .card-front .brand {
    position: absolute;
    left: 34px;
    top: 150px;
    display: flex;
    align-items: center;
    gap: 10px;
    color: var(--grey-text);
    font-weight: 300;
    font-size: 26px;
    letter-spacing: 2px;
    text-transform: uppercase;
  }
  .contact {
    position: absolute;
    right: 30px;
    bottom: 22px;
    list-style: none;
    text-align: right;
    color: var(--white);
    font-size: 11.5px;
    line-height: 1.45;
  }
  .contact li { display: flex; justify-content: flex-end; align-items: center; gap: 6px; }
  .contact .gap { margin-top: 10px; }
  .contact svg { width: 12px; height: 12px; fill: var(--white); flex: none; }
</style>
</head>
<body>

  <section class="card card-back" aria-label="Business card back">
    <div class="brand"><span class="brand-square"></span>KJ Automation</div>
    <p class="website">www.kjautomation.com.mx</p>
  </section>

  <section class="card card-front" aria-label="Business card front">
    <svg class="diagonal" viewBox="0 0 560 320" preserveAspectRatio="none" aria-hidden="true">
      <polygon points="560,18 560,26 130,320 118,320" fill="var(--grey)"/>
      <polygon points="560,40 560,320 150,320" fill="var(--blue)"/>
    </svg>

    <div class="person">
      <div class="person-name">LUIS MORENO</div>
      <div class="person-role">PRESIDENT</div>
    </div>

    <div class="brand"><span class="brand-square"></span>KJ Automation</div>

    <ul class="contact">
      <li>Av. Los Robles No. 418</li>
      <li>Col. Jardines C.P. 45120</li>
      <li>San Mateo, Jalisco, Mexico</li>
      <li>(+52) 33-5550-1427
        <svg viewBox="0 0 24 24"><path d="M6.6 10.8a15 15 0 0 0 6.6 6.6l2.2-2.2c.3-.3.7-.4 1-.2 1.1.4 2.3.6 3.6.6.6 0 1 .4 1 1V20c0 .6-.4 1-1 1A17 17 0 0 1 3 4c0-.6.4-1 1-1h3.5c.6 0 1 .4 1 1 0 1.3.2 2.5.6 3.6.1.3 0 .7-.2 1z"/></svg>
      </li>
      <li>33-5550-9082
        <svg viewBox="0 0 24 24"><path d="M7 1h10a2 2 0 0 1 2 2v18a2 2 0 0 1-2 2H7a2 2 0 0 1-2-2V3a2 2 0 0 1 2-2zm0 3v14h10V4zm5 15.5a1 1 0 1 0 0 2 1 1 0 0 0 0-2z"/></svg>
      </li>
      <li class="gap">lmoreno@kjautomation.com.mx
        <svg viewBox="0 0 24 24"><path d="M2 5h20v14H2zm2 2v.5l8 5 8-5V7zm0 3v7h16v-7l-8 5z"/></svg>
      </li>
    </ul>
  </section>

</body>
</html>
```